"Lantern Field" Play - Poster Design for Theatre Group

We are an amateur theatre group based in Geneva, Switzerland. We take pride in eye-catching posters for our shows, which are printed in various sizes.
This design will be for a play in March 2016. The play is called "Lantern Field", and it's a Harwick Medal winner from Marcus Ellery-Pound. The play is about a couple who have everything a family could want, until they lose a child in a life-shattering accident that turns their world upside down. The play charts the couple's bittersweet search to find each other and to find comfort.
Most importantly, we want a design that will make people want to see the show. We don't want to give away the plot or be too heavy-handed about death, but we want it to be clear that it's not a comedy (although there are some lighter moments!).
Attached you will find a template for the poster. This simply has our group name and logo in the top right corner: (Lakeshore Stage Players Circle presents).
You may change the color of both the text and the logo, but please do not change the font, size, or location.
Here is the information that needs to be on the poster, wherever you see fit:
play title: Lantern Field
author byline: by Marcus Ellery-Pound
director line: directed by Rob Feltwick
tagline: How do you keep it together when your whole world's fallen apart?
dates and times:
1-5 March 2016
(Tue-Fri 20:00, Sat 19:00)
location:
Théâtre du Vieux-Moulin
Eaux-Vives, Geneva
websites:
www.lspc.ch
www.scenelettres.ch
Technical Details:
Any font or combination of fonts is acceptable. The largest text should be the play title. The author's name must be at least 50% of the title font size.
For this competition, we would like the version with A3 proportions, which will also be used at F4 (89.5 x 128 cm) and A5 sizes (14.8 x 21 cm). Therefore no text should be below 9pt at A5.
However, from the winning designer we will also need repurposed sizes of the same design. Here is a comprehensive list of the sizes we will need.
1) A3 print poster. Artwork should be 300dpi, CMYK, sent with a 1mm bleed all round, to specification PDF/X-1A:2001. We will need this image in PDF format in addition to the default Artbrigade formats.
2) Chatterly advert picture. 1200px by 628px, RGB jpeg. This must comply with Chatterly’s restrictions on amount of text, which is no more than 20% of area taken up by text.(https://www.chatterly.example/ads/tools/text_overlay).
Because of these restrictions it is sufficient to include just the title and the author's name in this version.
3) Chatterly cover picture: 851px by 314px. RGB jpeg. It is sufficient to include just the title and the author's name in this version.
4) Web banner. 1000px by 300px. RGB jpeg. This version should include just the main image(s), no text.
Theatergoers
Entertainment

```html
<!DOCTYPE html>
<html lang="en">
<head>
<meta charset="utf-8">
<title>Lantern Field – Lakeshore Stage Players Circle</title>
<link rel="stylesheet" href="https://fonts.googleapis.com/css2?family=Oswald:wght@600&family=Quicksand:wght@400&display=swap">
<style>
  :root {
    --page: #ffffff;
    --ink-dark: #15181a;
    --ink-glow: #34454b;
    --text-light: #dcdcdc;
    --text-bold: #cfcfcf;
    --red-main: #7e0906;
    --red-deep: #520505;
  }
  * { margin: 0; padding: 0; box-sizing: border-box; }
  html, body {
    width: 1200px; height: 1200px; overflow: hidden;
    background: var(--page);
  }
  .poster {
    position: absolute; left: 178px; top: 28px;
    width: 809px; height: 1142px; overflow: hidden;
    background:
      radial-gradient(ellipse 48% 42% at 52% 50%, var(--ink-glow) 0%, rgba(40,55,60,0.45) 45%, rgba(21,24,26,0) 100%),
      linear-gradient(180deg, #121416 0%, var(--ink-dark) 50%, #111315 100%);
  }
  .info-bold {
    position: absolute;
    font-family: "Oswald", "Arial Narrow", sans-serif;
    font-weight: 600; color: var(--text-bold);
    letter-spacing: 0.2px;
  }
  .websites { left: 112px; top: 46px; font-size: 19px; line-height: 28px; }
  .presenter {
    right: 165px; top: 84px; font-size: 22px; line-height: 29.5px; text-align: right;
  }
  .presenter-mark {
    position: absolute; left: 668px; top: 66px;
    width: 100px; height: 100px; border-radius: 50%;
    border: 3px solid #bdbdbd;
  }
  .tagline {
    position: absolute; left: 0; top: 262px; width: 100%;
    text-align: center;
    font-family: "Quicksand", "Century Gothic", sans-serif;
    font-size: 36px; line-height: 50px; color: var(--text-light);
  }
  .key-art {
    position: absolute; left: 204px; top: 420px;
    width: 400px; height: 370px;
    background: radial-gradient(circle at 52% 50%, var(--red-deep) 0%, var(--red-main) 38%, rgba(126,9,6,0.35) 52%, rgba(21,24,26,0) 68%);
  }
  .title, .byline {
    position: absolute; left: 0; width: 100%; text-align: center;
    font-family: "Quicksand", "Century Gothic", sans-serif;
    font-weight: 400; color: var(--text-light);
    white-space: nowrap;
  }
  .title { top: 830px; font-size: 96px; line-height: 110px; padding-left: 10px; }
  .byline { top: 965px; font-size: 50px; line-height: 58px; padding-left: 10px; }
  .director { right: 91px; top: 1030px; font-size: 24px; line-height: 32px; }
  .schedule { left: 212px; top: 1070px; font-size: 19px; line-height: 27px; }
  .schedule .times { margin-left: 26px; }
</style>
</head>
<body>
  <main class="poster">
    <div class="info-bold websites">www.lspc.ch<br>www.scenelettres.ch</div>

    <div class="info-bold presenter">Lakeshore Stage<br>Players Circle<br>presents</div>
    <div class="presenter-mark" aria-hidden="true"></div>

    <p class="tagline">How do you keep it together<br>when your whole world's fallen apart?</p>

    <div class="key-art" role="img" aria-label="Key art: a deep red circular hole glowing in the dark"></div>

    <h1 class="title">Lantern Field</h1>
    <p class="byline">by Marcus Ellery-Pound</p>

    <p class="info-bold director">directed by Rob Feltwick</p>
    <p class="info-bold schedule">1-5 March 2016<span class="times">(Tue-Fri 20:00, Sat 19:00)</span><br>Théâtre du Vieux-Moulin Eaux-Vives, Geneva</p>
  </main>
</body>
</html>
```